Information poster for parquet showroom

We are a parquet shop from germany and need some information poster for our showroom, to show our costumers some important information about parqut directly. The three posters are about reasons for parquet, and there are two types of paper on the subject. We would like to place the posters in a wooden frame. The design should be modern but simple. Enclosed I send you some of my ideas but it does not have to be like this. Can be completely different. I also send you some pictures of our showroom. 1st poster: Why parquet (dimension: 90x130 cm) Why parquet? - brings nature into your home - ecologically sustainable raw material - pleasantly warm - timeless% 26amp; high quality optics - durable% 26amp; reparable flooring - improved indoor climate - unique ride 2. Advantages oiled - tangible wood structure - natural appearance - scratches less present - partial repair possible advantage varnished - very easy-care - classic% 26amp; elegant appearance - protection against dirt and moisture - variable gloss level 3. Poster: overview of the hardness of different kinds of wood (dimension: 67x130 cm) wood hardness according to Brinell in N / mm² maple europ. 28 maple canadian. 35 birch 27 beech 33 oak 34 alder 17 ash 37 doussie 42 spruce 12 kambala 30 chestnut 18 pine 20 cherry european. 31 Larch 19 Merbau 44 Robinia 48 Sucupira 57 Elm 30 Wenge 45

```html
<!DOCTYPE html>
<html lang="de">
<head>
<meta charset="utf-8">
<title>Warum Parkett? – Infoposter</title>
<link href="https://fonts.googleapis.com/css2?family=Bebas+Neue&display=swap" rel="stylesheet">
<style>
  :root {
    --page-bg: #eceef0;
    --frame-wood: #9a5a2a;
    --frame-wood-dark: #7a4420;
    --poster-white: #ffffff;
    --ink: #1c1c1c;
    --accent: #f39200;
    --plank-light: #e3e0dc;
    --plank-mid: #cfcbc6;
    --plank-dark: #b9b4ae;
  }
  * { margin: 0; padding: 0; box-sizing: border-box; }
  html, body {
    width: 1200px;
    height: 554px;
    overflow: hidden;
    background: var(--page-bg);
  }
  .stage {
    position: relative;
    width: 1200px;
    height: 554px;
  }
  .poster-frame {
    position: absolute;
    left: 415px;
    top: 12px;
    width: 370px;
    height: 530px;
    padding: 10px;
    background: linear-gradient(135deg, var(--frame-wood), var(--frame-wood-dark));
    box-shadow: 0 6px 18px rgba(0,0,0,0.25);
  }
  .poster {
    position: relative;
    width: 350px;
    height: 510px;
    background: var(--poster-white);
    overflow: hidden;
    font-family: 'Bebas Neue', 'Arial Narrow', sans-serif;
  }
  .poster-header {
    position: absolute;
    left: 0; top: 0;
    width: 350px;
    height: 160px;
    background: var(--poster-white);
  }
  .header-illustration {
    position: absolute;
    left: 14px;
    top: 24px;
    width: 86px;
    height: 112px;
    background: linear-gradient(160deg, #e9c99b, #c8955a 60%, #a8723e);
    clip-path: polygon(30% 0, 100% 55%, 80% 100%, 0 78%);
  }
  .headline {
    position: absolute;
    left: 108px;
    top: 22px;
    line-height: 0.88;
    color: var(--ink);
  }
  .headline-top {
    display: block;
    font-size: 84px;
    letter-spacing: 1px;
  }
  .headline-bottom {
    display: block;
    font-size: 44px;
    margin-top: 4px;
    margin-left: 18px;
  }
  .headline-accent { color: var(--accent); }
  .headline-mark { color: var(--ink); margin-left: 10px; font-size: 50px; }
  .plank-field {
    position: absolute;
    left: 0; top: 160px;
    width: 350px;
    height: 350px;
    background:
      repeating-linear-gradient(180deg, transparent 0 33px, rgba(120,112,104,0.25) 33px 34px),
      linear-gradient(180deg, var(--plank-light), var(--plank-mid) 55%, var(--plank-dark));
  }
  .benefit-list { list-style: none; }
  .benefit {
    position: absolute;
    height: 30px;
    width: 262px;
    background: var(--poster-white);
    color: var(--ink);
    font-size: 16px;
    line-height: 31px;
    padding: 0 12px;
    white-space: nowrap;
    box-shadow: 0 3px 6px rgba(0,0,0,0.22);
  }
  .benefit--left { left: 0; }
  .benefit--right { right: 0; text-align: left; }
  .benefit--wide { width: 278px; }
  .benefit em { font-style: normal; color: var(--accent); }
</style>
</head>
<body>
<main class="stage">
  <div class="poster-frame">
    <article class="poster">
      <header class="poster-header">
        <div class="header-illustration" role="img" aria-label="Illustration gestapelter Parkettdielen"></div>
        <h1 class="headline">
          <span class="headline-top">Warum</span>
          <span class="headline-bottom"><span class="headline-accent">Parkett</span><span class="headline-mark">?</span></span>
        </h1>
      </header>
      <section class="plank-field" role="img" aria-label="Hintergrund aus hellgrauen Holzdielen">
        <ul class="benefit-list">
          <li class="benefit benefit--left" style="top:18px;">Holt die <em>Natur</em> in Ihr Zuhause</li>
          <li class="benefit benefit--right" style="top:72px;"><em>Ökologisch</em> nachhaltiger Rohstoff</li>
          <li class="benefit benefit--left" style="top:126px;">Angenehm <em>fußwarm</em></li>
          <li class="benefit benefit--right" style="top:180px;"><em>Zeitlose</em> &amp; hochwertige Optik</li>
          <li class="benefit benefit--left benefit--wide" style="top:234px;">Langlebiger &amp; <em>reparabler</em> Bodenbelag</li>
          <li class="benefit benefit--right" style="top:288px;">Einzigartiges <em>Laufgefühl</em></li>
        </ul>
      </section>
    </article>
  </div>
</main>
</body>
</html>
```